I want to revise my business card design and get a more modern and up to date design.

Brolvane Handyman Sevices originated from a family-owned and operated contractor business, performing home renovation, addition, and construction work in the NYC area since 2004. Today, we specialize in reliable and affordable handyman services for residential and commercial clients In 2014, we expanded to northern New Jersey. In 2016, we brought quality home improvement and repair services to new Bucks County, PA, and nearby New Jersey areas.
Target Market(s)
Home owners and business that might be looking for a General contractor, handyman, cleaning services and Home maintenance and property.
Industry/Entity Type
Construction Company
Contact Information for Business Card
I am open to new ideas
Colors
Designer to choose colors to be used in the design.
Look and feel
Each slider illustrates characteristics of the customer's brand and the style your logo design should communicate.

```html
<!DOCTYPE html>
<html lang="en">
<head>
<meta charset="utf-8">
<title>Brolvane Handyman Sevices – Business Card</title>
<link rel="stylesheet" href="https://fonts.googleapis.com/css2?family=Cinzel:wght@400;700&family=Open+Sans:wght@400;600;700&display=swap">
<style>
  :root {
    --stage: #1e1e1e;
    --card: #262626;
    --card-edge: #2d2d2d;
    --accent: #e3202a;
    --text: #f2f2f2;
    --ghost: #2e2e2e;
  }
  * { box-sizing: border-box; margin: 0; padding: 0; }
  html, body { width: 1200px; height: 895px; overflow: hidden; }
  body {
    background: var(--stage);
    font-family: "Open Sans", sans-serif;
    color: var(--text);
    display: flex;
    flex-direction: column;
    align-items: center;
    justify-content: center;
    gap: 40px;
  }
  .card {
    position: relative;
    width: 640px;
    height: 366px;
    background: var(--card);
    border: 1px solid var(--card-edge);
    overflow: hidden;
  }
  .card__band {
    position: absolute;
    left: 0; right: 0; bottom: 0;
    height: 9px;
    background: var(--accent);
  }

  /* Front */
  .front__decoration {
    position: absolute;
    left: 40px; top: 120px;
    width: 220px; height: 240px;
    border-radius: 50% 50% 20% 20%;
    background: radial-gradient(circle at 50% 40%, var(--ghost), var(--card) 70%);
  }
  .brand {
    position: absolute;
    left: 180px; top: 120px;
    display: flex;
    align-items: center;
    gap: 18px;
  }
  .brand__mark {
    width: 72px; height: 72px;
    border-radius: 50%;
    background: #3a3a3a;
  }
  .brand__name {
    font-weight: 700;
    font-size: 58px;
    line-height: 1;
    color: #d9d9d9;
    letter-spacing: -1px;
  }
  .brand__tagline {
    margin-top: 8px;
    font-size: 13px;
    letter-spacing: 6px;
    color: #d9d9d9;
    text-transform: uppercase;
  }

  /* Back */
  .identity {
    position: absolute;
    left: 28px; right: 28px; top: 118px;
    display: flex;
    align-items: center;
    justify-content: center;
    gap: 22px;
  }
  .person { text-align: right; white-space: nowrap; }
  .person__name {
    font-family: "Cinzel", serif;
    font-size: 24px;
    color: var(--accent);
    line-height: 1.1;
  }
  .person__role {
    font-size: 15px;
    color: var(--text);
    margin-top: 2px;
  }
  .divider {
    width: 2px; height: 44px;
    background: var(--text);
    flex: none;
  }
  .contact { list-style: none; font-size: 14.5px; line-height: 1.6; white-space: nowrap; }
  .contact li { display: flex; align-items: center; gap: 9px; }
  .contact svg { width: 13px; height: 13px; flex: none; }
  .services {
    position: absolute;
    left: 24px; right: 24px; top: 228px;
    text-align: center;
    font-size: 16px;
    line-height: 1.6;
  }
  .services__sep { color: var(--accent); padding: 0 8px; }
</style>
</head>
<body>

  <section class="card card--front">
    <div class="front__decoration" role="img" aria-label="Faint enlarged brand mascot decoration"></div>
    <div class="brand">
      <div class="brand__mark"></div>
      <div>
        <div class="brand__name">Brolvane</div>
        <div class="brand__tagline">Handyman Sevices</div>
      </div>
    </div>
    <div class="card__band"></div>
  </section>

  <section class="card card--back">
    <div class="identity">
      <div class="person">
        <div class="person__name">TEODORO MARQUEZ</div>
        <div class="person__role">Owner</div>
      </div>
      <div class="divider"></div>
      <ul class="contact">
        <li>
          <svg viewBox="0 0 14 14" aria-hidden="true"><rect x="3.5" y="1" width="7" height="12" rx="1.2" fill="none" stroke="#e3202a" stroke-width="1.6"/><circle cx="7" cy="10.8" r="0.8" fill="#e3202a"/></svg>
          (215) 555-0148
        </li>
        <li>
          <svg viewBox="0 0 14 14" aria-hidden="true"><rect x="1" y="3" width="12" height="8.5" fill="#e3202a"/><path d="M1 3 L7 8 L13 3" fill="none" stroke="#262626" stroke-width="1.2"/></svg>
          brolvanehandymannyc@mailbox.com
        </li>
      </ul>
    </div>
    <p class="services">
      General contractor, Property maintenance, Cleaning and handyman services<br>
      Repair<span class="services__sep">|</span>Improve<span class="services__sep">|</span>Maintain<span class="services__sep">|</span>Remodel
    </p>
    <div class="card__band"></div>
  </section>

</body>
</html>
```